Business Cards using attached files

Please make new business cards using files attached. I would like something a little more updated possibly. Double sided.
I am wanting to make sure I can change the names and positions easily myself.

Target Market(s)

Automotive Repair

Industry/Entity Type

Automotive

Contact Information for Business Card

See attached files

Font styles to use
Serif

Colors
0054AA
0677BA
7BADD7
CADEEF
E8F1F8

Requirements
Must have
• Red white blue colors
Nice to have
• I'd like it slightly updated from our existing design. Double sided. I'd like to be able to change names and positions easily to have them printed.
Should not have
• I'm not sure

```html
<!DOCTYPE html>
<html lang="en">
<head>
<meta charset="utf-8">
<title>Ridgeway Auto &amp; Truck Center — Business Card</title>
<link rel="stylesheet" href="https://fonts.googleapis.com/css2?family=Tinos:wght@400;700&display=swap">
<style>
  :root {
    --red: #d62e35;
    --navy: #264463;
    --ink: #1d1d1d;
    --paper: #ffffff;
    --backdrop: #3a3a3a;
    --map-tone: #e9eef4;
    --social-1: #3b5a9a;
    --social-2: #4aa6e0;
    --social-3: #d94a3d;
  }
  * { box-sizing: border-box; margin: 0; padding: 0; }
  html, body { width: 1200px; height: 1059px; overflow: hidden; }
  body {
    background: var(--backdrop);
    font-family: "Tinos", "Times New Roman", serif;
    color: var(--ink);
    position: relative;
  }
  .card {
    position: absolute;
    width: 690px;
    height: 392px;
    background: var(--paper);
    overflow: hidden;
  }
  .card--front { left: 255px; top: 100px; }
  .card--back { left: 255px; top: 537px; }

  /* Front */
  .tagline {
    position: absolute; left: 34px; top: 34px;
    font-size: 37.5px; font-weight: 700; color: var(--red);
    white-space: nowrap;
  }
  .name-bar {
    position: absolute; left: 0; top: 115px; width: 13px; height: 41px;
    background: var(--red);
  }
  .person { position: absolute; left: 34px; top: 110px; }
  .person__name { font-size: 29px; font-weight: 700; color: var(--navy); line-height: 1.1; }
  .person__first { color: var(--red); }
  .person__title { font-size: 15.5px; margin-top: 2px; }
  .address { position: absolute; left: 34px; top: 187px; font-size: 15.5px; line-height: 17px; font-style: normal; }
  .contacts { position: absolute; left: 34px; top: 242px; list-style: none; font-size: 15.5px; }
  .contacts li { display: flex; align-items: center; height: 20.5px; }
  .contacts svg { width: 12px; height: 12px; margin-right: 6px; fill: var(--red); }
  .brand {
    position: absolute; left: 411px; top: 115px; width: 240px; height: 178px;
    display: flex; align-items: center; justify-content: center; gap: 12px;
  }
  .brand__dot { width: 22px; height: 22px; border-radius: 50%; background: var(--red); }
  .brand__name { font-size: 44px; font-weight: 700; color: var(--navy); }
  .rule { position: absolute; left: 34px; top: 323px; width: 620px; height: 1px; background: var(--red); }
  .services {
    position: absolute; left: 34px; top: 343px; width: 620px;
    font-size: 16px; letter-spacing: 0.95px; white-space: nowrap;
  }

  /* Back */
  .location-panel {
    position: absolute; left: 0; top: 0; width: 314px; height: 100%;
    background: var(--navy); color: #fff; text-align: center;
  }
  .location-map {
    position: absolute; left: 26px; top: 29px; width: 262px; height: 259px;
    border: 4px solid #111;
    background: linear-gradient(160deg, #f4f6f9, var(--map-tone));
  }
  .location-name { position: absolute; left: 0; right: 0; top: 299px; font-size: 19.5px; font-weight: 700; white-space: nowrap; }
  .location-address { position: absolute; left: 0; right: 0; top: 328px; font-size: 19.5px; font-weight: 700; line-height: 22px; }
  .promise { position: absolute; left: 314px; top: 0; right: 0; height: 100%; }
  .promise__title {
    position: absolute; left: 0; right: 0; top: 24px; text-align: center;
    font-size: 21px; font-weight: 700; color: var(--red);
  }
  .promise__list { position: absolute; left: 20px; top: 66px; list-style: none; font-size: 16px; }
  .promise__list li { height: 26.8px; display: flex; align-items: center; }
  .promise__list li::before {
    content: ""; width: 5px; height: 5px; border-radius: 50%; background: #111; margin-right: 9px;
  }
  .online__label { position: absolute; left: 0; right: 0; top: 308px; text-align: center; font-size: 16px; }
  .online__site { position: absolute; left: 22px; top: 343px; font-size: 16px; white-space: nowrap; }
  .online__icons { position: absolute; left: 212px; top: 336px; display: flex; gap: 5px; }
  .online__icons span { width: 36px; height: 36px; border-radius: 50%; }
  .online__icons span:nth-child(1) { background: var(--social-1); }
  .online__icons span:nth-child(2) { background: var(--social-2); }
  .online__icons span:nth-child(3) { background: var(--social-3); }
</style>
</head>
<body>
  <section class="card card--front">
    <h1 class="tagline">Family Owned &amp; Operated Since 1991</h1>
    <div class="name-bar"></div>
    <div class="person">
      <div class="person__name"><span class="person__first">Daniel</span> Corvino</div>
      <div class="person__title">General Manager</div>
    </div>
    <address class="address">418 Harbor Road<br>Millbrook, NY 11990</address>
    <ul class="contacts">
      <li><svg viewBox="0 0 24 24"><path d="M6.6 10.8a15 15 0 0 0 6.6 6.6l2.2-2.2a1 1 0 0 1 1-.25 11.4 11.4 0 0 0 3.6.57 1 1 0 0 1 1 1V20a1 1 0 0 1-1 1A17 17 0 0 1 3 4a1 1 0 0 1 1-1h3.5a1 1 0 0 1 1 1c0 1.25.2 2.45.57 3.6a1 1 0 0 1-.25 1z"/></svg>(555) 208-4417</li>
      <li><svg viewBox="0 0 24 24"><path d="M6 2h12v5H6zM3 8h18a1 1 0 0 1 1 1v7h-4v6H6v-6H2V9a1 1 0 0 1 1-1zm5 8v4h8v-4z"/></svg>(555) 208-4418</li>
      <li><svg viewBox="0 0 24 24"><path d="M2 5h20v14H2zm2 2v.5l8 5.5 8-5.5V7l-8 5.5z"/></svg>Dan@ridgewayauto.com</li>
    </ul>
    <div class="brand">
      <span class="brand__dot"></span>
      <span class="brand__name">Ridgeway</span>
    </div>
    <div class="rule"></div>
    <p class="services">Auto Service - Inspections - Lube/Oil Service - Diesel - Fleet - DOT - Truck - Trailer</p>
  </section>

  <section class="card card--back">
    <div class="location-panel">
      <div class="location-map" role="img" aria-label="Street map showing the shop location near the local routes and parkway"></div>
      <div class="location-name">Ridgeway Auto &amp; Truck Center</div>
      <div class="location-address">418 Harbor Road<br>Millbrook, NY 11990</div>
    </div>
    <div class="promise">
      <h2 class="promise__title">We Stand Behind Our Service</h2>
      <ul class="promise__list">
        <li>Family Owned &amp; Operated</li>
        <li>Complimentary 2 year/24,000 mile warranty</li>
        <li>Free local pickup/dropoff service</li>
        <li>Experts In Domestic &amp; Import Service</li>
        <li>Master Certified Mechanics</li>
        <li>Diesel &amp; Fleet Services Available</li>
        <li>Honest, Knowledgeable, Trustworthy Service</li>
        <li>Top Rated A+ Auto Repair Facility</li>
      </ul>
      <div class="online__label">Find Us Online:</div>
      <div class="online__site">www.ridgewayauto.com</div>
      <div class="online__icons"><span></span><span></span><span></span></div>
    </div>
  </section>
</body>
</html>
```